indépendant en tant que Massothérapeute et Préparateur Mental, j'ai besoin de ...

Massothérapeute et préparateur mental indépendant, je recherche une carte de visite sobre et dynamique, sans images liées au massage ou à la préparation mentale mais intégrant mon logo. Les couleurs que j'aime bien sont : Blanc, gris, anthracite, noir et jaune

carte de préférence Horizontale
neutre qui puisse toucher le deux domaines Massothérapie et préparation mentale

Requirements
Must have
• mon projet doit intégrer au recto:
LOGO
Loïc Bardemaz
078 315 26 48
info@loicbardemaz-exemple.ch
et éventuellement www.loicbardemaz-exemple.ch

et au verso les deux adresses:

Chemin des Grèvelins 7B
1450 Valmorens-le-Lac

Avenue des Mélèzes 9
1790 Praz-Fleuri

Should not have
• mon projet ne doit pas contenir d'image en liens avec le massage ni la préparation mentale.

```html
<!DOCTYPE html>
<html lang="fr">
<head>
<meta charset="utf-8">
<title>Loïc Bardemaz – cartes de visite</title>
<link href="https://fonts.googleapis.com/css2?family=Arimo:wght@400;700&display=swap" rel="stylesheet">
<style>
  :root{
    --stage:#e2e2e2;
    --paper:#ffffff;
    --ink:#111111;
    --edge:#333333;
    --on-ink:#ffffff;
  }
  *{box-sizing:border-box;margin:0;padding:0}
  html,body{width:1200px;height:547px;overflow:hidden}
  body{
    background:var(--stage);
    font-family:"Arimo",Arial,sans-serif;
    color:var(--ink);
    position:relative;
  }
  .card{
    position:absolute;
    top:120px;
    width:540px;height:308px;
    background:var(--paper);
    border:1px solid var(--edge);
    box-shadow:4px 6px 10px rgba(0,0,0,.25);
    overflow:hidden;
  }
  .card--front{left:40px}
  .card--back{left:620px}

  .brand-mark{
    position:absolute;right:26px;top:30px;
    width:56px;height:56px;background:var(--ink);
  }

  .brand{position:absolute;left:34px;top:38px;display:flex;align-items:center;gap:10px}
  .brand__square{width:34px;height:34px;background:var(--ink)}
  .brand__name{font-weight:700;font-size:19px;line-height:1}
  .brand__tagline{font-size:7.5px;letter-spacing:.3px;margin-top:3px;text-transform:uppercase}

  .holder{position:absolute;left:40px;top:122px;font-size:28px;font-weight:700}

  .contacts{position:absolute;left:0;top:174px;list-style:none}
  .contacts li{display:flex;align-items:center;height:23px;margin-bottom:9px;font-size:19px}
  .contacts .tab{
    width:73px;height:23px;background:var(--ink);
    display:flex;justify-content:flex-end;align-items:center;padding-right:6px;margin-right:8px;
  }
  .contacts svg{width:18px;height:16px}

  .locations__title{position:absolute;left:36px;top:42px;font-size:19px;font-weight:700;letter-spacing:.2px}
  .location{
    position:absolute;left:0;width:403px;height:84px;background:var(--ink);color:var(--on-ink);
    display:flex;align-items:center;font-size:19px;line-height:1.35;
  }
  .location--first{top:88px}
  .location--second{top:179px}
  .location svg{width:22px;height:30px;margin:0 26px 0 36px;flex:none}
</style>
</head>
<body>

<section class="card card--front" aria-label="Recto">
  <div class="brand">
    <span class="brand__square"></span>
    <div>
      <div class="brand__name">Loïc Bardemaz</div>
      <div class="brand__tagline">Massothérapeute / Préparateur Mental</div>
    </div>
  </div>
  <div class="brand-mark"></div>
  <h1 class="holder">Loïc Bardemaz</h1>
  <ul class="contacts">
    <li><span class="tab"><svg viewBox="0 0 18 16"><rect x="1" y="2" width="16" height="13" rx="2" fill="#fff"/><rect x="3" y="0" width="12" height="5" rx="2" fill="#fff"/><circle cx="9" cy="10" r="3" fill="#111"/></svg></span>078 315 26 48</li>
    <li><span class="tab"><svg viewBox="0 0 18 16"><rect x="1" y="2" width="16" height="12" fill="#fff"/><path d="M1 2l8 7 8-7" stroke="#111" stroke-width="1.5" fill="none"/></svg></span>info@loicbardemaz-exemple.ch</li>
    <li><span class="tab"><svg viewBox="0 0 18 16"><circle cx="9" cy="8" r="7" fill="none" stroke="#fff" stroke-width="1.4"/><ellipse cx="9" cy="8" rx="3" ry="7" fill="none" stroke="#fff" stroke-width="1.2"/><path d="M2 8h14M3 4.5h12M3 11.5h12" stroke="#fff" stroke-width="1.1"/></svg></span>www.loicbardemaz-exemple.ch</li>
  </ul>
</section>

<section class="card card--back" aria-label="Verso">
  <div class="brand-mark"></div>
  <h2 class="locations__title">NOS EMPLACEMENTS</h2>
  <div class="location location--first">
    <svg viewBox="0 0 22 30"><path d="M11 0C5 0 0 5 0 11c0 8 11 19 11 19s11-11 11-19C22 5 17 0 11 0z" fill="#fff"/><circle cx="11" cy="11" r="4.5" fill="#111"/></svg>
    <p>Chemin des Grèvelins 7B<br>1450 Valmorens-le-Lac</p>
  </div>
  <div class="location location--second">
    <svg viewBox="0 0 22 30"><path d="M11 0C5 0 0 5 0 11c0 8 11 19 11 19s11-11 11-19C22 5 17 0 11 0z" fill="#fff"/><circle cx="11" cy="11" r="4.5" fill="#111"/></svg>
    <p>Avenue des Mélèzes 9<br>1790 Praz-Fleuri</p>
  </div>
</section>

</body>
</html>
```